automotive repair and collision repair shop card

our company is called K.R Motor service we are a automotive repair company
we also do government inspections. the company information is on the cards. I would like you to use my new logo and create a new card and use the information from my old card. Good Luck!!

Industry/Entity Type

Car Repair

Contact Information for Business Card

Address: #417-15862 91 Ave, Surrey, BC V5T 8K4
Phone:(604) 555-0187
fax 604 555 0142
website www.krmotor.example

Font styles to use
Serif
Sans Serif

Requirements
Must have
• all the information
Should not have
• the owner and there name

```html
<!DOCTYPE html>
<html lang="en">
<head>
<meta charset="utf-8">
<title>K.R Motor service – Business Card</title>
<link href="https://fonts.googleapis.com/css2?family=Exo+2:wght@400;600&display=swap" rel="stylesheet">
<style>
  :root {
    --stage: #2b2b2b;
    --card-dark: #0d0d0d;
    --card-light: #ffffff;
    --ink: #1a1a1a;
    --ink-soft: #4a4a4a;
    --steel: #5c5c5c;
    --ghost: #efefef;
  }
  * { box-sizing: border-box; margin: 0; padding: 0; }
  html, body { width: 1200px; height: 819px; overflow: hidden; }
  body {
    background: var(--stage);
    font-family: "Exo 2", sans-serif;
    display: flex;
    align-items: center;
    justify-content: center;
    gap: 60px;
  }
  .card {
    position: relative;
    width: 520px;
    height: 300px;
    overflow: hidden;
    box-shadow: 0 10px 30px rgba(0,0,0,.45);
  }

  /* Front */
  .card--front { background: var(--card-dark); }
  .card--front .car-art {
    position: absolute; left: 110px; top: 50px; width: 300px; height: 120px;
    border-radius: 60px 90px 20px 20px;
    background: linear-gradient(180deg, #3a3a3a, #222);
  }
  .card--front .brand {
    position: absolute; left: 0; right: 0; top: 186px; text-align: center;
    font-weight: 600; font-size: 34px; line-height: 40px; color: var(--steel);
  }
  .card--front .tagline {
    position: absolute; left: 0; right: 0; top: 230px; text-align: center;
    font-weight: 400; font-size: 15px; color: var(--steel);
  }

  /* Back */
  .card--back { background: var(--card-light); }
  .card--back .ghost-art {
    position: absolute; left: 250px; top: 14px; width: 250px; height: 40px;
    border-radius: 30px 60px 10px 10px;
    background: linear-gradient(180deg, var(--ghost), #f7f7f7);
  }
  .card--back .ghost-name {
    position: absolute; left: 0; right: 0; bottom: 14px; text-align: center;
    font-weight: 600; font-size: 44px; line-height: 50px; color: var(--ghost);
    white-space: nowrap;
  }
  .card--back .logo-block {
    position: absolute; left: 18px; top: 78px; width: 190px; text-align: center;
  }
  .card--back .car-art {
    width: 160px; height: 62px; margin: 0 auto;
    border-radius: 30px 45px 10px 10px;
    background: linear-gradient(180deg, #6a6a6a, #2e2e2e);
  }
  .card--back .brand {
    margin-top: 8px;
    font-weight: 600; font-size: 19px; color: var(--ink);
    white-space: nowrap;
  }
  .card--back .tagline {
    margin-top: 2px; font-size: 12px; color: var(--ink-soft);
  }
  .card--back .divider {
    position: absolute; left: 222px; top: 64px; width: 1px; height: 150px;
    background: var(--ink);
  }
  .contact {
    position: absolute; left: 240px; top: 66px;
    list-style: none; font-size: 15px; line-height: 21px; color: var(--ink);
  }
  .contact li { display: flex; align-items: flex-start; gap: 7px; }
  .contact svg { flex: none; margin-top: 5px; }
</style>
</head>
<body>

  <section class="card card--front" aria-label="Card front">
    <div class="car-art" role="img" aria-label="Illustration of a sports car in profile"></div>
    <div class="brand">K.R Motor service</div>
    <div class="tagline">One Stop Repair Shop</div>
  </section>

  <section class="card card--back" aria-label="Card back">
    <div class="ghost-art" role="img" aria-label="Faint large sports car illustration"></div>
    <div class="ghost-name" aria-hidden="true">K.R Motor service</div>

    <div class="logo-block">
      <div class="car-art" role="img" aria-label="Illustration of a sports car in profile"></div>
      <div class="brand">K.R Motor service</div>
      <div class="tagline">One Stop Repair Shop</div>
    </div>

    <div class="divider"></div>

    <ul class="contact">
      <li>
        <svg width="12" height="12" viewBox="0 0 12 12" aria-hidden="true"><path d="M2 1h3l1 3-2 1a7 7 0 0 0 3 3l1-2 3 1v3a1 1 0 0 1-1 1A10 10 0 0 1 1 2a1 1 0 0 1 1-1z" fill="var(--ink-soft)"/></svg>
        <span>(604) 555-0187</span>
      </li>
      <li>
        <svg width="12" height="12" viewBox="0 0 12 12" aria-hidden="true"><rect x="3" y="0.5" width="6" height="4" fill="var(--ink-soft)"/><rect x="0.5" y="4" width="11" height="5" fill="var(--ink-soft)"/><rect x="3" y="8" width="6" height="3.5" fill="var(--ink-soft)"/></svg>
        <span>Fax 604 555 0142</span>
      </li>
      <li>
        <svg width="12" height="12" viewBox="0 0 12 12" aria-hidden="true"><rect x="0.5" y="2" width="11" height="8" fill="var(--ink-soft)"/><path d="M1 2.5l5 4 5-4" stroke="#fff" fill="none"/></svg>
        <span>info@krmotor.example</span>
      </li>
      <li>
        <svg width="12" height="12" viewBox="0 0 12 12" aria-hidden="true"><circle cx="6" cy="6" r="5.5" fill="var(--ink-soft)"/><path d="M1 6h10M6 1c-2 3-2 7 0 10M6 1c2 3 2 7 0 10" stroke="#fff" stroke-width=".8" fill="none"/></svg>
        <span>www.krmotor.example</span>
      </li>
      <li>
        <svg width="12" height="12" viewBox="0 0 12 12" aria-hidden="true"><path d="M6 0a4 4 0 0 1 4 4c0 3-4 8-4 8S2 7 2 4a4 4 0 0 1 4-4z" fill="var(--ink-soft)"/><circle cx="6" cy="4" r="1.5" fill="#fff"/></svg>
        <span>#417-15862 91 Ave Surrey<br>BC V5T 8K4</span>
      </li>
    </ul>
  </section>

</body>
</html>
```